Eye catching business card

2 sided
Black background with logo in color on one side along with the words "Proudly serving the commercial and defense industries since 1975"
2nd side to contain contact information (see attached current business card) and "Waterjet, Composite, Precision Machining and Clean Room Manufacturing" with a very faint watermark of a waving USA Flag in the back ground.
Remove the "est. 195" from the current logo design

```html
<!DOCTYPE html>
<html lang="en">
<head>
<meta charset="utf-8">
<title>Meridian Machine – Business Card</title>
<link href="https://fonts.googleapis.com/css2?family=Raleway:wght@300;700&family=Arimo:wght@400;700&display=swap" rel="stylesheet">
<style>
  :root {
    --stage: #2a2a2d;
    --card: #141416;
    --text-light: #d9d9dc;
    --text-mid: #a9a9ae;
    --blue: #2f8fe0;
    --blue-deep: #2a62c9;
    --blue-bright: #38a9f0;
  }
  * { margin: 0; padding: 0; box-sizing: border-box; }
  html, body { width: 1200px; height: 800px; overflow: hidden; background: var(--stage); }
  .stage { position: relative; width: 1200px; height: 800px; }

  .card {
    position: absolute; width: 520px; height: 298px;
    background: var(--card); border-radius: 16px; overflow: hidden;
    box-shadow: 0 18px 40px rgba(0,0,0,.45);
    font-family: "Arimo", Arial, sans-serif; color: var(--text-light);
  }
  .card--front { left: 70px; top: 90px; }
  .card--back { left: 610px; top: 412px; }

  .band {
    position: absolute; left: 0; right: 0; bottom: 0;
    background: linear-gradient(90deg, var(--blue-deep), var(--blue-bright) 50%, var(--blue-deep));
  }
  .card--front .band { height: 10px; }
  .card--back .band { height: 34px; display: flex; align-items: center; justify-content: center;
    font-size: 13px; color: #0f2a4a; letter-spacing: .2px; }

  /* Front */
  .star-field {
    position: absolute; inset: 0;
    background: linear-gradient(160deg, #232326 0%, #1a1a1c 55%, var(--card) 100%);
  }
  .front-content { position: absolute; left: 0; right: 0; top: 58px; text-align: center; }
  .brand-name { font-family: "Raleway", sans-serif; font-weight: 700; font-size: 26px;
    letter-spacing: 1.5px; color: var(--text-light); white-space: nowrap; }
  .tagline { margin-top: 26px; font-family: "Raleway", sans-serif; font-size: 19px; line-height: 1.35;
    color: var(--text-mid); font-weight: 300; letter-spacing: .5px; }
  .tagline strong { font-weight: 700; color: var(--text-light); }

  /* Back */
  .flag-wash {
    position: absolute; left: 0; top: 0; width: 100%; height: 264px;
    background: radial-gradient(ellipse 60% 70% at 28% 60%, #222226 0%, #19191b 55%, var(--card) 100%);
  }
  .back-brand { position: absolute; left: 22px; top: 128px; width: 256px;
    display: flex; align-items: center; justify-content: center; gap: 9px; }
  .back-brand .square { width: 16px; height: 16px; background: var(--blue); flex: none; }
  .back-brand .brand-name { font-size: 19px; letter-spacing: 1px; }
  .divider { position: absolute; left: 290px; top: 50px; width: 1px; height: 150px;
    background: linear-gradient(var(--blue), rgba(47,143,224,.2)); }
  .contact { position: absolute; left: 310px; top: 44px; font-size: 12.5px; line-height: 1.45; color: var(--text-light); }
  .contact .name { font-size: 16px; font-weight: 700; letter-spacing: .5px; }
  .contact .role { color: var(--blue); font-size: 13px; margin-bottom: 6px; }
  .contact ul { list-style: none; margin-top: 6px; }
  .contact li { display: flex; align-items: center; gap: 7px; }
  .contact svg { width: 11px; height: 11px; fill: var(--blue); flex: none; }
  .company-line { position: absolute; right: 26px; bottom: 44px; font-size: 17px; font-weight: 700; color: var(--text-light); }
</style>
</head>
<body>
<main class="stage">

  <section class="card card--front" aria-label="Card front">
    <div class="star-field" role="img" aria-label="Faint star pattern background"></div>
    <div class="front-content">
      <div class="brand-name">MERIDIAN MACHINE INC</div>
      <p class="tagline">PROUDLY SERVING<br><strong>THE DEFENSE AND</strong><br>COMMERCIAL INDUSTRIES<br><strong>SINCE 1975</strong></p>
    </div>
    <div class="band"></div>
  </section>

  <section class="card card--back" aria-label="Card back">
    <div class="flag-wash" role="img" aria-label="Very faint waving USA flag watermark"></div>
    <div class="back-brand">
      <span class="square"></span><span class="brand-name">MERIDIAN MACHINE INC</span>
    </div>
    <div class="divider"></div>
    <div class="contact">
      <div class="name">DANIEL HARTLEY</div>
      <div class="role">President</div>
      <div>412 Harbor Mill Rd.</div>
      <div>Glen Arden, PA 17200</div>
      <ul>
        <li><svg viewBox="0 0 24 24"><path d="M6.6 10.8a15 15 0 0 0 6.6 6.6l2.2-2.2a1 1 0 0 1 1-.25 11.4 11.4 0 0 0 3.6.6 1 1 0 0 1 1 1V20a1 1 0 0 1-1 1A17 17 0 0 1 3 4a1 1 0 0 1 1-1h3.5a1 1 0 0 1 1 1c0 1.25.2 2.45.6 3.6a1 1 0 0 1-.25 1z"/></svg>410-555-0148</li>
        <li><svg viewBox="0 0 24 24"><path d="M6 3h12v5H6zM4 9h16a2 2 0 0 1 2 2v6h-4v4H6v-4H2v-6a2 2 0 0 1 2-2zm4 7v3h8v-3z"/></svg>410-555-0162</li>
        <li><svg viewBox="0 0 24 24"><path d="M2 5h20v14H2zm2 2v.5l8 5 8-5V7z"/></svg>dan@meridianmachine.com</li>
        <li><svg viewBox="0 0 24 24"><circle cx="12" cy="12" r="10"/></svg>www.meridianmachine.com</li>
      </ul>
    </div>
    <div class="company-line">Meridian Machine, Inc.</div>
    <div class="band">Waterjets, Composites &amp; Precision Machining &amp; Clean Room Manufacturing</div>
  </section>

</main>
</body>
</html>
```